Brochure Design Project for Family and Cosmetic Dental Practice

Family and Cosmetic Dental Practice with Ocean/Tropical Theme
Here is some more information about my business. We also have a website :www.marlowcrestsmiles.com. That has a video that we made and gives you a some more information about us.

An Overview / Background of the Business & Services :

Family and Cosmetic Dental Practice

Procedures that we do:

Clearmora (Clear Braces)

Dentures and Partials

Whitening/ Teeth Bleaching (both Brite and Vel)

Cosmetic Dentistry (veneers and esthetic crowns)

Implants

Children's Dentistry

Sedation Dentistry and Nitrous Oxide Gas (Laughing Gas)

The Target Market / Audience you are trying to reach:

Families (30 to 40 yrs with children) - Caucasians and Hispanics
People seeking cosmetic dentistry
Older Patients (50yrs +)

Design Specifics; any preferences or ideas for Style, Colour, Imagery, etc :

Color: Blues

Theme: Ocean/ Tropical

Our Philosophy

Our belief is that the best oral care that you receive is at home where you are able to maintain your oral hygiene through proper brushing, flossing and control of your diet. We would like to see you maintain your natural teeth for the rest of your life. When this is not possible we will work with you to replace them with the best aesthetic and functional restorative dentistry
that is available.

We want to let people we have been at our location for 10 years and we are family owned and are here for the long run. We are active in the community

Bios of the doctors: ( I already sent the headshot photos)

Dr Leonard Whitcombe
“Dr. Lenny”

Dr. Lenny Whitcombe attended Pemberton University for his undergraduate studies and earned a Bachelor’s degree in Chemistry. While attending Pemberton he pursued his passion of running and was a member of two Prairie Athletic League Champion cross country teams. His passion for running evolved into a desire to compete in triathlons. He continued his interest in the sciences and working with his hands by attending the Ashgrove State University College of Dentistry where he met his wife, Clara Whitcombe D.D.S. and earned his D.D.S. with honors in Oral Surgery. He has practiced the last few years in Tucson treating a wide range of patients. His desire to practice dentistry revolves around the patient and service. Some of his hobby highlights include finishing the Desert Ridge Endurance triathlon in 11 hours and 37 minutes in 2005 and a single digit golf handicap. His current passion is mountain biking. He recently finished the Ridgecrest Trail Cycling race (100 miles in one day)! Lately he spends a lot of time caring for and playing with his 3 daughters. Dr. Lenny Whitcombe is also a member of NOA (National Oral Alliance), StOC (State Oral Care Society) and GPF (Guild of Practice Fellows).

Dr. Clara Whitcombe
“Dr. Whitcombe”

Dr. Clara Whitcombe attended both Halvern College and Eastbrook Wesleyan College for her undergraduate degrees. She received a Bachelor of Science in Biology and a Bachelor of Arts in Psychology. After college, Dr Whitcombe worked for several years in the dental field while continuing her education by working towards a Master’s degree in Cell and Molecular Biology. At this point in her life Dr. Whitcombe knew that she enjoyed the dental field and decided to attend dental school. Dr. Whitcombe completed her Doctorate of Dental Surgery (D.D.S.) at Ashgrove State University where she met her husband, Dr. Leonard Whitcombe. They then moved to Tucson, Arizona in order to be close to family. When Dr. Clara isn't in the office creating beautiful smiles, she is busy with her 3 daughters and their numerous activities. Dr. Clara Whitcombe has additional training in the areas of endodontics and oral sedation. She is also a member of The National Guild of Practice Fellows (NGPF), National Oral Alliance (NOA), and State Oral Care Society (StOC). In her time outside of the office, Dr. Whitcombe enjoys traveling, spending time with her family, working out and being involved with book club.
Let me know if you need anything else!

Target Market(s)

See above

Industry/Entity Type

Business

Colors
33a6d7
85cae6
33b8a4

Requirements
Must have
• Testimonials taken from Rateway reviews. In any images used, the people must have nice smiles and teeth.

```html
<!DOCTYPE html>
<html lang="en">
<head>
<meta charset="utf-8">
<title>Marlowcrest Family Dentistry – Trifold Brochure</title>
<link rel="stylesheet" href="https://fonts.googleapis.com/css2?family=Raleway:wght@300;600&family=Open+Sans:ital,wght@0,400;0,600;0,700;1,400&family=Kaushan+Script&display=swap">
<style>
:root{
  --blue:#33a6d7;
  --blue-deep:#1c8fcf;
  --blue-soft:#85cae6;
  --teal:#33b8a4;
  --sky:#dcefF7;
  --sand:#e9dfcf;
  --ink:#2b3440;
  --body:#4a5562;
  --bg:#6b7078;
  --white:#ffffff;
}
*{box-sizing:border-box;margin:0;padding:0}
html,body{width:872px;height:1200px;overflow:hidden}
body{background:var(--bg);font-family:"Open Sans",Arial,sans-serif;position:relative}
.sheet{position:absolute;left:28px;width:816px;height:556px;display:flex;box-shadow:0 10px 30px rgba(0,0,0,.35)}
.sheet--outside{top:28px}
.sheet--inside{top:616px;background:linear-gradient(180deg,#d6ecf6 0%,#eef6f9 38%,#f6f6f3 60%,#fbfbfa 100%)}
.panel{position:relative;width:272px;height:556px;overflow:hidden}
.panel+.panel{box-shadow:inset 6px 0 10px -6px rgba(0,0,0,.18)}
.photo{position:absolute}

/* Outside: philosophy */
.panel--philosophy{background:var(--blue-deep)}
.panel--philosophy .photo{left:0;top:0;width:272px;height:250px;background:linear-gradient(160deg,#4c5866,#8b8f94 45%,#d9d2c6)}
.panel--philosophy svg{position:absolute;left:0;top:0}
.philosophy__title{position:absolute;left:26px;top:214px;color:var(--white);font:300 24px/1.05 Raleway,sans-serif;letter-spacing:.5px}
.philosophy__text{position:absolute;left:26px;top:282px;width:222px;color:var(--white);font-size:8px;line-height:1.55}
.philosophy__text p+p{margin-top:10px}

/* Outside: contact */
.panel--contact{background:linear-gradient(180deg,#e4f1f7 0%,#b8dcec 30%,#7fc0de 55%,#5eb2d9 70%)}
.contact__intro{position:absolute;top:46px;left:40px;width:192px;text-align:center;font-style:italic;font-size:9.5px;line-height:1.35;color:var(--ink)}
.contact__map{left:61px;top:150px;width:150px;height:150px;border-radius:50%;background:radial-gradient(circle,#eeeeea,#cfd0cc);border:5px solid rgba(255,255,255,.85);box-shadow:0 3px 10px rgba(0,0,0,.25)}
.panel--contact svg.band{position:absolute;left:0;top:0}
.contact__details{position:absolute;left:28px;top:372px;width:220px;color:var(--white)}
.contact__address{font-size:12px;line-height:1.45}
.contact__phone{font:700 24px/1.2 "Open Sans",sans-serif;margin-top:10px;letter-spacing:.3px}
.contact__web{font-size:11px;margin-top:8px}

/* Outside: cover */
.panel--cover{background:linear-gradient(180deg,#cfe7f3 0%,#a9d3e7 30%,#d7e4e6 60%,var(--sand) 78%,#e3d7c4 100%)}
.brand{position:absolute;left:30px;top:34px;display:flex;align-items:center;gap:10px}
.brand__mark{width:44px;height:44px;background:var(--ink)}
.brand__name{font:600 17px/1.05 Raleway,sans-serif;color:var(--ink);letter-spacing:2px;text-transform:uppercase}
.cover__family{left:22px;top:110px;width:236px;height:210px;border-radius:40px;background:radial-gradient(ellipse at 50% 45%,#e7cdb8 0%,#c9b2a1 40%,rgba(220,230,234,.0) 75%)}
.cover__tagline{position:absolute;left:20px;top:380px;width:236px;font:400 25px/1.2 "Kaushan Script",cursive;color:var(--ink);text-align:center}
.cover__web{position:absolute;left:0;top:480px;width:272px;text-align:center;font-size:11.5px;color:var(--ink)}

/* Inside shared */
.section-title{font:300 23px/1 Raleway,sans-serif;color:var(--ink);text-transform:uppercase}
.circle{border-radius:50%;border:5px solid var(--white);box-shadow:0 3px 8px rgba(0,0,0,.2)}

/* Inside: services */
.services__photo{left:58px;top:34px;width:156px;height:156px;background:linear-gradient(150deg,#f2f2f2,#b9c0c6 55%,#e8eaec)}
.services .section-title{position:absolute;left:28px;top:246px}
.services__list{position:absolute;left:28px;top:284px;list-style:none;font-size:10px;color:var(--ink)}
.services__list li{display:flex;align-items:center;gap:8px;height:19px}
.services__list svg{flex:none}

/* Inside: doctors */
.doctors .section-title{position:absolute;left:24px;top:30px}
.doctor{position:absolute;left:18px;width:236px;font-size:7.6px;line-height:1.5;color:var(--body)}
.doctor--first{top:66px}
.doctor--second{top:300px}
.doctor__photo{float:left;position:relative;width:62px;height:62px;margin:4px 8px 2px 0;background:linear-gradient(160deg,#d9c2ae,#b59a86)}
.doctor__name{font-weight:700;font-size:9px;color:var(--ink);text-align:right;margin-bottom:2px}
.doctors__rule{position:absolute;left:24px;top:284px;width:224px;height:1px;background:#b9c4cc}

/* Inside: testimonials */
.testimonials__photo--one{left:72px;top:22px;width:150px;height:150px;background:linear-gradient(160deg,#6d5a4d,#c9a58b 55%,#eadcd0)}
.testimonials__photo--two{left:40px;top:150px;width:104px;height:104px;background:linear-gradient(160deg,#4a3a33,#d2b19a 60%,#ecdccf)}
.testimonials .section-title{position:absolute;left:26px;top:270px}
.testimonial{position:absolute;left:26px;width:220px;font-style:italic;font-size:8.3px;line-height:1.5;color:var(--body)}
.testimonial--first{top:302px;padding-left:26px}
.testimonial--second{top:400px}
.quote-mark{position:absolute;font:700 40px/1 Georgia,serif;color:#b7c2ca}
.quote-mark--open{left:26px;top:296px}
.quote-mark--close{left:226px;top:478px}
.testimonials__rule{position:absolute;left:26px;top:390px;width:220px;height:1px;background:#b9c4cc}
</style>
</head>
<body>

<section class="sheet sheet--outside" aria-label="Brochure outside">
  <article class="panel panel--philosophy">
    <div class="photo" role="img" aria-label="Photo of the two dentists standing in the practice reception area"></div>
    <svg width="272" height="556" viewBox="0 0 272 556" aria-hidden="true">
      <path d="M0 250 Q110 170 272 58 L272 556 L0 556 Z" fill="#1c8fcf"/>
      <path d="M0 238 Q110 158 272 46" fill="none" stroke="#85cae6" stroke-width="8" opacity=".8"/>
    </svg>
    <h2 class="philosophy__title">OUR<br>PHILOSOPHY</h2>
    <div class="philosophy__text">
      <p>Our belief is that the best oral care that you receive is at home where you are able to maintain your oral hygiene through proper brushing, flossing and control of your diet. We would like to see you maintain your natural teeth for the rest of your life. When this is not possible we will work with you to replace them with the best aesthetic and functional restorative dentistry that is available.</p>
      <p>We will help to educate you on what is occurring in your mouth and will discuss how to maintain good oral hygiene or what is needed in order to get your mouth back to a healthy state. We encourage you to ask questions about the treatment that you need so that you will have a good understanding of your oral health.</p>
    </div>
  </article>

  <article class="panel panel--contact">
    <p class="contact__intro">We encourage you to contact us with any questions or comments you may have</p>
    <svg class="band" width="272" height="556" viewBox="0 0 272 556" aria-hidden="true">
      <path d="M0 320 Q140 290 272 330 L272 556 L0 556 Z" fill="#1c8fcf"/>
      <path d="M0 312 Q140 282 272 322" fill="none" stroke="#85cae6" stroke-width="5" opacity=".7"/>
    </svg>
    <div class="photo circle contact__map" role="img" aria-label="Street map showing the practice location"></div>
    <div class="contact__details">
      <p class="contact__address">1482 West Harbor Palm Drive<br>Suite 210, Marlow, AZ 85301</p>
      <p class="contact__phone">480-555-0172</p>
      <p class="contact__web">www.marlowcrestsmiles.com</p>
    </div>
  </article>

  <article class="panel panel--cover">
    <div class="brand">
      <span class="brand__mark"></span>
      <span class="brand__name">Marlowcrest<br>Family<br>Dentistry</span>
    </div>
    <div class="photo cover__family" role="img" aria-label="Smiling family of four on a beach"></div>
    <p class="cover__tagline">Quality Dentistry With a Compassionate Touch</p>
    <p class="cover__web">www.marlowcrestsmiles.com</p>
  </article>
</section>

<section class="sheet sheet--inside" aria-label="Brochure inside">
  <article class="panel services">
    <div class="photo circle services__photo" role="img" aria-label="Dental instruments on a tray"></div>
    <h2 class="section-title">Services</h2>
    <ul class="services__list">
      <li><svg width="11" height="11" viewBox="0 0 11 11"><circle cx="5.5" cy="5.5" r="5" fill="none" stroke="#33a6d7"/><path d="M3 5.6l1.8 1.8L8.2 3.8" fill="none" stroke="#33a6d7" stroke-width="1.4"/></svg>Cleaning</li>
      <li><svg width="11" height="11" viewBox="0 0 11 11"><circle cx="5.5" cy="5.5" r="5" fill="none" stroke="#33a6d7"/><path d="M3 5.6l1.8 1.8L8.2 3.8" fill="none" stroke="#33a6d7" stroke-width="1.4"/></svg>Cosmetic Dentistry</li>
      <li><svg width="11" height="11" viewBox="0 0 11 11"><circle cx="5.5" cy="5.5" r="5" fill="none" stroke="#33a6d7"/><path d="M3 5.6l1.8 1.8L8.2 3.8" fill="none" stroke="#33a6d7" stroke-width="1.4"/></svg>Composite (White) Fillings</li>
      <li><svg width="11" height="11" viewBox="0 0 11 11"><circle cx="5.5" cy="5.5" r="5" fill="none" stroke="#33a6d7"/><path d="M3 5.6l1.8 1.8L8.2 3.8" fill="none" stroke="#33a6d7" stroke-width="1.4"/></svg>Porcelain Crowns (Caps)</li>
      <li><svg width="11" height="11" viewBox="0 0 11 11"><circle cx="5.5" cy="5.5" r="5" fill="none" stroke="#33a6d7"/><path d="M3 5.6l1.8 1.8L8.2 3.8" fill="none" stroke="#33a6d7" stroke-width="1.4"/></svg>Dental Implants</li>
      <li><svg width="11" height="11" viewBox="0 0 11 11"><circle cx="5.5" cy="5.5" r="5" fill="none" stroke="#33a6d7"/><path d="M3 5.6l1.8 1.8L8.2 3.8" fill="none" stroke="#33a6d7" stroke-width="1.4"/></svg>Veneers</li>
      <li><svg width="11" height="11" viewBox="0 0 11 11"><circle cx="5.5" cy="5.5" r="5" fill="none" stroke="#33a6d7"/><path d="M3 5.6l1.8 1.8L8.2 3.8" fill="none" stroke="#33a6d7" stroke-width="1.4"/></svg>Tooth Whitening</li>
      <li><svg width="11" height="11" viewBox="0 0 11 11"><circle cx="5.5" cy="5.5" r="5" fill="none" stroke="#33a6d7"/><path d="M3 5.6l1.8 1.8L8.2 3.8" fill="none" stroke="#33a6d7" stroke-width="1.4"/></svg>Brite and Vel</li>
      <li><svg width="11" height="11" viewBox="0 0 11 11"><circle cx="5.5" cy="5.5" r="5" fill="none" stroke="#33a6d7"/><path d="M3 5.6l1.8 1.8L8.2 3.8" fill="none" stroke="#33a6d7" stroke-width="1.4"/></svg>Clearmora (clear braces)</li>
      <li><svg width="11" height="11" viewBox="0 0 11 11"><circle cx="5.5" cy="5.5" r="5" fill="none" stroke="#33a6d7"/><path d="M3 5.6l1.8 1.8L8.2 3.8" fill="none" stroke="#33a6d7" stroke-width="1.4"/></svg>Dentures/Partial</li>
      <li><svg width="11" height="11" viewBox="0 0 11 11"><circle cx="5.5" cy="5.5" r="5" fill="none" stroke="#33a6d7"/><path d="M3 5.6l1.8 1.8L8.2 3.8" fill="none" stroke="#33a6d7" stroke-width="1.4"/></svg>Children's Dentistry</li>
      <li><svg width="11" height="11" viewBox="0 0 11 11"><circle cx="5.5" cy="5.5" r="5" fill="none" stroke="#33a6d7"/><path d="M3 5.6l1.8 1.8L8.2 3.8" fill="none" stroke="#33a6d7" stroke-width="1.4"/></svg>Cionscious Sedation (for anxiety reduction)</li>
      <li><svg width="11" height="11" viewBox="0 0 11 11"><circle cx="5.5" cy="5.5" r="5" fill="none" stroke="#33a6d7"/><path d="M3 5.6l1.8 1.8L8.2 3.8" fill="none" stroke="#33a6d7" stroke-width="1.4"/></svg>Emergency Treatment</li>
    </ul>
  </article>

  <article class="panel doctors">
    <h2 class="section-title">Our Doctors</h2>
    <div class="doctor doctor--first">
      <div class="doctor__photo circle" role="img" aria-label="Headshot of Dr Leonard Whitcombe"></div>
      <h3 class="doctor__name">Dr Leonard Whitcombe</h3>
      <p>Dr. Lenny Whitcombe attended Pemberton University for his undergraduate studies and earned a Bachelor's degree in Chemistry. While attending Pemberton he pursued his passion of running and was a member of two Prairie Athletic League Champion cross country teams. He continued his interest in the sciences and working with his hands by attending the Ashgrove State University College of Dentistry where he met his wife, Clara Whitcombe D.D.S. and earned his D.D.S. with honors in Oral Surgery.</p>
    </div>
    <div class="doctors__rule"></div>
    <div class="doctor doctor--second">
      <div class="doctor__photo circle" role="img" aria-label="Headshot of Dr. Clara Whitcombe"></div>
      <h3 class="doctor__name">Dr. Clara Whitcombe</h3>
      <p>Dr. Clara Whitcombe attended both Halvern College and Eastbrook Wesleyan College for her undergraduate degrees. She received a Bachelor of Science in Biology and a Bachelor of Arts in Psychology. After college, Dr Whitcombe worked for several years in the dental field while continuing her education by working towards a Master's degree in Cell and Molecular Biology. Dr. Whitcombe completed her Doctorate of Dental Surgery (D.D.S.) at Ashgrove State University.</p>
    </div>
  </article>

  <article class="panel testimonials">
    <div class="photo circle testimonials__photo--one" role="img" aria-label="Smiling man with bright healthy teeth"></div>
    <div class="photo circle testimonials__photo--two" role="img" aria-label="Smiling woman with bright healthy teeth"></div>
    <h2 class="section-title">Testimonials</h2>
    <span class="quote-mark quote-mark--open" aria-hidden="true">&ldquo;</span>
    <p class="testimonial testimonial--first">By far the best dentists I have been too! Both Dr. Whitcombes are an absolute joy to see. The staff treats you like family every time you walk in the door. Marlowcrest Family Dentistry makes going to the dentist a pleasure. If you are looking for new dentist or are new to the area.....this is the place you want. A+ all the way.</p>
    <div class="testimonials__rule"></div>
    <p class="testimonial testimonial--second">Marlowcrest Family Dentistry offers superior care! Both dentists are well-educated, caring, professionals who are looking to build lasting relationships with their patients! They give honest second opinions too! If you haven't received excellent care from a dentist in the past, contact Marlowcrest Family Dentistry in Marlow for an appointment!</p>
    <span class="quote-mark quote-mark--close" aria-hidden="true">&rdquo;</span>
  </article>
</section>

</body>
</html>
```